Vantorique Business Card and Letter Head

We are a leadership assessment consultancy based in Sydney, Australia. We help executive-level decison-makers select leaders for more senior level roles in corporate and government organisations. Our methodology is based on the latest research from the field of neuroscience.
We need a business card design and matching letter head that presents our company, Vantorique, as a:
1. trusted adviser to senior executive-level decison makers
2. niche consultancy who are experts in the field of assessing leadership talent
3. results-focused solution provider who balance scientific methods with pragmatic solutions
The following company details should be used in all designs:
Company Name: Vantorique
Details (for business card):
Daniel Prewett
High Potential Officer
Level 17, Marrowby Tower
14 Tallowin Square
Sydney, NSW 2000 Australia
Phone: 1300 582 714
Mobile: 0412 637 208
Email: daniel.prewett@vantorique.com.au
Website: vantorique.com.au
I have attached the logo for Vantorique (for both a white and black background) - your business card and letter head designs must incoporate this logo and colour scheme.
Thanks for your interest in this project, I'm looking forward to receiving your ideas.
Regards,
Daniel
Target Market(s)
Executive-level decison-makers in corporate and government organisations (e.g., CEO, VP, Head of Human Resources)
Industry/Entity Type
Leadership
Look and feel
Each slider illustrates characteristics of the customer's brand and the style your logo design should communicate.

```html
<!DOCTYPE html>
<html lang="en">
<head>
<meta charset="utf-8">
<title>Vantorique Business Card and Letterhead</title>
<link href="https://fonts.googleapis.com/css2?family=Arimo:wght@400;700&display=swap" rel="stylesheet">
<style>
  :root {
    --canvas: #8a8a8a;
    --paper: #d6d7d9;
    --card-dark: #2a2a2d;
    --ink: #2f2f31;
    --ink-light: #e4e4e4;
    --accent: #c1271a;
    --mark-faint: #cbcccd;
  }
  * { margin: 0; padding: 0; box-sizing: border-box; }
  html, body { width: 1198px; height: 1200px; overflow: hidden; }
  body {
    position: relative;
    background: var(--canvas);
    font-family: "Arimo", Arial, sans-serif;
    color: var(--ink);
  }
  .sheet { position: absolute; background: var(--paper); }
  .letterhead { left: 378px; top: 52px; width: 779px; height: 1100px; }
  .card-front { position: absolute; left: 58px; top: 242px; width: 637px; height: 364px; background: var(--card-dark); }
  .card-back { left: 60px; top: 630px; width: 634px; height: 364px; }

  .wordmark {
    position: absolute;
    display: flex; align-items: center; gap: 14px;
    font-weight: 700; letter-spacing: -0.5px; line-height: 1;
  }
  .wordmark .badge { display: block; background: var(--accent); }
  .letterhead .wordmark { left: 50px; top: 62px; font-size: 44px; color: var(--ink); }
  .letterhead .wordmark .badge { width: 26px; height: 26px; }
  .card-front .wordmark { left: 146px; top: 160px; font-size: 46px; color: var(--ink-light); }
  .card-front .wordmark .badge { width: 28px; height: 28px; }
  .card-back .wordmark { left: 32px; top: 286px; font-size: 32px; color: var(--ink); gap: 10px; }
  .card-back .wordmark .badge { width: 20px; height: 20px; }

  .faint-square { position: absolute; background: var(--mark-faint); }
  .letterhead .faint-square { left: 430px; top: 55px; width: 300px; height: 300px; }
  .card-back .faint-square { left: 400px; top: 128px; width: 204px; height: 204px; }

  .text-block { position: absolute; font-weight: 700; font-size: 13px; line-height: 16px; }
  .align-right { text-align: right; }
  .holder { left: 31px; top: 36px; font-size: 16px; line-height: 20px; }
  .holder .name { text-transform: uppercase; letter-spacing: 0.3px; }
  .card-back .contact { right: 34px; top: 34px; font-size: 14px; line-height: 16.5px; }
  .card-back .address { right: 34px; top: 281px; font-size: 14px; line-height: 16.5px; }
  .letterhead .address { left: 54px; top: 1013px; }
  .letterhead .contact { right: 52px; top: 995px; }
</style>
</head>
<body>
  <section class="sheet letterhead" aria-label="Letterhead">
    <div class="faint-square" aria-hidden="true"></div>
    <div class="wordmark"><span class="badge"></span>Vantorique</div>
    <address class="text-block address" style="font-style:normal">
      Level 17, Marrowby Tower<br>14 Tallowin Square<br>Sydney, NSW 2000 Australia
    </address>
    <div class="text-block contact align-right">
      Phone: 1300 582 714<br>Mobile: 0412 637 208<br>Email: daniel.prewett@vantorique.com.au<br>Website: vantorique.com.au
    </div>
  </section>

  <section class="card-front" aria-label="Business card front">
    <div class="wordmark"><span class="badge"></span>Vantorique</div>
  </section>

  <section class="sheet card-back" aria-label="Business card back">
    <div class="faint-square" aria-hidden="true"></div>
    <div class="text-block holder">
      <div class="name">Daniel Prewett</div>
      <div class="role">High Potential Officer</div>
    </div>
    <div class="text-block contact align-right">
      Phone: 1300 582 714<br>Mobile: 0412 637 208<br>Email: daniel.prewett@vantorique.com.au<br>Website: vantorique.com.au
    </div>
    <address class="text-block address align-right" style="font-style:normal">
      Level 17, Marrowby Tower<br>14 Tallowin Square<br>Sydney, NSW 2000 Australia
    </address>
    <div class="wordmark"><span class="badge"></span>Vantorique</div>
  </section>
</body>
</html>
```